Day Spa Web Design Project

We just created a blog to add to our main site. We need the colors to match our main site and the look and feel of the blog to be smoother and less ameture looking, like the examples below.

Main Site, match this color scheme:
http://www.fernlowdayspa.com/

The project site:
http://blog.fernlowdayspa.com/

Our industry leaders blog site is our comparative and examples of what we need:
http://blog.relaxquest.com/
http://blog.purewellnessjournal.com/
http://thecoralbayblog.com/ (i like the layout a lot)
http://www.kneadhaven.com/blog/

Requirements
Must have
• social sharing.
Responsive design (already has it just keep it)
appealing mobile front page

```html
<!DOCTYPE html>
<html lang="en">
<head>
<meta charset="utf-8">
<title>Fernlow Blog</title>
<link href="https://fonts.googleapis.com/css2?family=Arimo:wght@400;700&display=swap" rel="stylesheet">
<style>
:root{
  --header:#0c0c0c;
  --pink:#f3ab9b;
  --sand:#f6e0c7;
  --cream:#fcefe1;
  --panel:#f4e4d2;
  --white:#ffffff;
  --accent:#c0392b;
  --date:#e08a6e;
  --text:#555555;
}
*{margin:0;padding:0;box-sizing:border-box}
html,body{width:726px;height:1200px;overflow:hidden}
body{position:relative;background:var(--cream);font-family:Arimo,Arial,sans-serif;color:var(--text);font-size:8px}
.abs{position:absolute}
.site-header{left:0;top:0;width:726px;height:61px;background:linear-gradient(#000,#1a1a1a)}
.brand{left:54px;top:19px;display:flex;align-items:center;gap:8px}
.brand-mark{width:14px;height:14px;background:var(--pink)}
.brand-name{color:#fff;font-size:22px;font-weight:700;line-height:1}
.nav-active{left:389px;top:0;width:42px;height:61px;background:linear-gradient(#1c1c1c,#3a3a3a)}
.nav a{position:absolute;top:33px;color:#fff;font-size:10px;text-decoration:none}
.hero-band{left:0;top:61px;width:726px;height:225px;background:var(--pink)}
.slider{left:54px;top:70px;width:618px;height:198px;background:#d9a89c;padding:4px;box-shadow:0 6px 8px rgba(0,0,0,.18)}
.slide{width:100%;height:100%;background:linear-gradient(90deg,#f6f6f6 0%,#fbfbfb 45%,#f1e3d6 72%,#f4ddc9 85%,#fafafa 100%)}
.slide-title{left:86px;top:115px;font-size:20px;font-weight:700;color:#a5a5a5}
.slide-nav{left:65px;top:243px}
.crumb-band{left:0;top:286px;width:726px;height:24px;background:var(--sand)}
.crumb{left:54px;top:294px;font-size:8px;color:#333}
.crumb a{color:var(--accent);text-decoration:none}
.card{width:204px;height:254px;background:var(--white);border:1px solid #f0e0d0;box-shadow:0 0 4px rgba(0,0,0,.08)}
.card-photo{position:absolute;left:12px;top:12px;width:180px;height:94px;border:3px solid #e9d9c9;border-radius:2px}
.card-title{position:absolute;left:14px;top:116px;color:var(--accent);font-size:8.6px}
.card-text{position:absolute;left:14px;top:128px;width:176px;font-size:7.6px;line-height:11.3px;text-align:justify;color:#666}
.card-date{position:absolute;left:14px;top:178px;font-size:7.6px;color:var(--date)}
.share-bar{position:absolute;left:12px;top:198px;width:180px;height:27px;background:#f2f2f2;border-radius:3px;display:flex;gap:3px;padding:5px 0 0 16px}
.share-bar i,.foot-share i{display:block;width:16px;height:16px;border-radius:2px}
.card-more{position:absolute;left:13px;top:236px;color:var(--accent);font-size:9px}
.s1{background:#f39a2c}.s2{background:#3fa9e0}.s3{background:#3b5b9a}.s4{background:#c9302c}.s5{background:#e5e5e5}.s6{background:#1b7bb8}.s7{background:#6a6a6a}.s8{background:#222}
.pager{left:54px;top:1103px;width:419px;height:28px;background:#fff;border:1px solid #f0e0d0;font-size:7px;color:#555}
.pager b{position:absolute;top:8px;width:14px;height:13px;border-radius:3px;background:#ddd;color:#fff;font-weight:400;text-align:center;line-height:13px;font-size:6.5px}
.side-box{left:483px;width:189px}
.side-head{position:absolute;left:11px;top:8px;font-size:11.5px;font-weight:700;color:#333}
.side-inner{position:absolute;left:5px;width:179px;background:#fff}
.dot{position:absolute;right:12px;top:9px;width:11px;height:11px;border-radius:50%;background:#b0a59a}
.post{position:absolute;left:12px;width:160px;font-size:7.4px;line-height:11.3px;color:#666;padding-left:11px}
.post::before{content:"››";position:absolute;left:0;top:0;color:#333}
.post em{display:block;font-style:normal;color:var(--date);margin-top:3px}
.friend{position:absolute;width:36px;text-align:center;font-size:5.8px;color:#666}
.friend span{display:block;width:34px;height:34px;margin:0 auto 3px;border:1px solid #ddd}
.field{position:absolute;left:11px;width:167px;height:18px;background:#fff;border:1px solid #e6d0c6;font-size:6.5px;color:#777;padding:5px 0 0 10px}
.site-footer{left:0;top:1144px;width:726px;height:56px;background:var(--sand)}
.foot-links{left:54px;top:1157px;font-size:8px;color:#333}
.foot-copy{left:54px;top:1177px;font-size:8px;color:#333}
.foot-share{left:522px;top:1163px;display:flex;gap:3px}
</style>
</head>
<body>
<header class="site-header abs">
  <div class="brand abs"><i class="brand-mark"></i><span class="brand-name">Fernlow</span></div>
  <div class="nav-active abs"></div>
  <nav class="nav">
    <a style="left:398px">Home</a><a style="left:452px">About</a><a style="left:506px">Services</a><a style="left:571px">Media</a><a style="left:626px">Categories</a>
  </nav>
</header>

<section class="hero-band abs"></section>
<div class="slider abs"><div class="slide" role="img" aria-label="Relaxed woman resting with a yellow lily beside soft white candles"></div></div>
<div class="slide-title abs">Healthy Essentials for Good Living</div>
<svg class="slide-nav abs" width="22" height="13" viewBox="0 0 22 13"><circle cx="6" cy="6.5" r="6" fill="#8a8a8a"/><circle cx="16" cy="6.5" r="6" fill="#8a8a8a"/><path d="M7.5 3.5L4.5 6.5 7.5 9.5Z M14.5 3.5L17.5 6.5 14.5 9.5Z" fill="#fff"/></svg>

<div class="crumb-band abs"></div>
<div class="crumb abs"><a>Home</a> &nbsp;»&nbsp; Welcome</div>

<article class="card abs" style="left:54px;top:325px"><div class="card-photo" role="img" aria-label="Head massage by candlelight" style="background:linear-gradient(135deg,#3b2414,#a0724a 55%,#3a2212)"></div><div class="card-title">Keys to stress reduction</div><p class="card-text">Some stress is natural, but often times stress becomes a problem when it leaves you feeling over-whelmed and out of control. Seventy seven percent of Americans report experiencing...</p><div class="card-date">April-14-2013</div><div class="share-bar"><i class="s1"></i><i class="s2"></i><i class="s3"></i><i class="s4"></i><i class="s5"></i><i class="s6"></i><i class="s7"></i><i class="s8"></i></div><div class="card-more">VIEW MORE &nbsp;»</div></article>
<article class="card abs" style="left:269px;top:325px"><div class="card-photo" role="img" aria-label="Spa pool with floating candles at dusk" style="background:linear-gradient(#2a2a26,#4b5a52 50%,#7a6a48)"></div><div class="card-title">Keys to stress reduction</div><p class="card-text">Some stress is natural, but often times stress becomes a problem when it leaves you feeling over-whelmed and out of control. Seventy seven percent of Americans report experiencing...</p><div class="card-date">April-14-2013</div><div class="share-bar"><i class="s1"></i><i class="s2"></i><i class="s3"></i><i class="s4"></i><i class="s5"></i><i class="s6"></i><i class="s7"></i><i class="s8"></i></div><div class="card-more">VIEW MORE &nbsp;»</div></article>
<article class="card abs" style="left:54px;top:585px"><div class="card-photo" role="img" aria-label="Stacked black stones on bath salt" style="background:linear-gradient(#cfe6e0,#6f8f8c 50%,#e4eeee)"></div><div class="card-title">Keys to stress reduction</div><p class="card-text">Some stress is natural, but often times stress becomes a problem when it leaves you feeling over-whelmed and out of control. Seventy seven percent of Americans report experiencing...</p><div class="card-date">April-14-2013</div><div class="share-bar"><i class="s1"></i><i class="s2"></i><i class="s3"></i><i class="s4"></i><i class="s5"></i><i class="s6"></i><i class="s7"></i><i class="s8"></i></div><div class="card-more">VIEW MORE &nbsp;»</div></article>
<article class="card abs" style="left:269px;top:585px"><div class="card-photo" role="img" aria-label="Treatment room with two massage beds" style="background:linear-gradient(135deg,#6b4a2c,#c7a27a 55%,#e8d5bd)"></div><div class="card-title">Keys to stress reduction</div><p class="card-text">Some stress is natural, but often times stress becomes a problem when it leaves you feeling over-whelmed and out of control. Seventy seven percent of Americans report experiencing...</p><div class="card-date">April-14-2013</div><div class="share-bar"><i class="s1"></i><i class="s2"></i><i class="s3"></i><i class="s4"></i><i class="s5"></i><i class="s6"></i><i class="s7"></i><i class="s8"></i></div><div class="card-more">VIEW MORE &nbsp;»</div></article>
<article class="card abs" style="left:54px;top:844px"><div class="card-photo" role="img" aria-label="Couple relaxing in a jacuzzi bath" style="background:linear-gradient(#7b6240,#b89a6e 55%,#d9cf9a)"></div><div class="card-title">Keys to stress reduction</div><p class="card-text">Some stress is natural, but often times stress becomes a problem when it leaves you feeling over-whelmed and out of control. Seventy seven percent of Americans report experiencing...</p><div class="card-date">April-14-2013</div><div class="share-bar"><i class="s1"></i><i class="s2"></i><i class="s3"></i><i class="s4"></i><i class="s5"></i><i class="s6"></i><i class="s7"></i><i class="s8"></i></div><div class="card-more">VIEW MORE &nbsp;»</div></article>
<article class="card abs" style="left:269px;top:844px"><div class="card-photo" role="img" aria-label="Woman resting beside a bowl of pink flowers" style="background:linear-gradient(135deg,#3c160e,#9a4a32 50%,#c8604e)"></div><div class="card-title">Keys to stress reduction</div><p class="card-text">Some stress is natural, but often times stress becomes a problem when it leaves you feeling over-whelmed and out of control. Seventy seven percent of Americans report experiencing...</p><div class="card-date">April-14-2013</div><div class="share-bar"><i class="s1"></i><i class="s2"></i><i class="s3"></i><i class="s4"></i><i class="s5"></i><i class="s6"></i><i class="s7"></i><i class="s8"></i></div><div class="card-more">VIEW MORE &nbsp;»</div></article>

<nav class="pager abs">
  <span class="abs" style="left:201px;top:10px">Page 1 of 32</span>
  <b style="left:243px;background:#8e8e8e">1</b><b style="left:259px">2</b><b style="left:275px">3</b><b style="left:291px">4</b><b style="left:307px">5</b><b style="left:323px">6</b><b style="left:339px">7</b><b style="left:355px">8</b><b style="left:371px">»</b>
  <span class="abs" style="left:389px;top:9px;color:#999">...</span><b style="left:398px">»»</b>
</nav>

<div class="side-box abs" style="top:325px;height:35px;background:var(--pink)"><div class="field" style="top:8px;height:19px">Search</div>
<svg class="abs" style="left:160px;top:12px" width="10" height="10" viewBox="0 0 10 10"><circle cx="4" cy="4" r="3" fill="none" stroke="#222" stroke-width="1.6"/><path d="M6.2 6.2L9 9" stroke="#222" stroke-width="1.8"/></svg></div>

<div class="side-box abs" style="top:366px;height:211px;background:var(--panel)"><div class="side-head">Recent post</div><i class="dot"></i>
<div class="side-inner" style="top:26px;height:181px">
 <p class="post" style="top:7px">Maecenas pharetra est sed enim vulpu tate sollicitudin. Nam neclar nunc nec arcu suscipit pulvinar posuere.<em>April-14-2013</em></p>
 <p class="post" style="top:64px">Maecenas pharetra est sed enim vulpu tate sollicitudin. Nam neclar nunc nec arcu suscipit pulvinar posuere.<em>April-14-2013</em></p>
 <p class="post" style="top:121px">Maecenas pharetra est sed enim vulpu tate sollicitudin. Nam neclar nunc nec arcu suscipit pulvinar posuere.<em>April-14-2013</em></p>
</div></div>

<div class="side-box abs" style="top:583px;height:180px;background:var(--panel)"><div class="side-head">Popular post</div><i class="dot"></i>
<div class="side-inner" style="top:26px;height:149px">
 <div class="abs" role="img" aria-label="Woman with a red flower in her hair relaxing on a spa bed" style="left:10px;top:8px;width:160px;height:70px;border:3px solid #f4d9c4;background:linear-gradient(135deg,#b99e8a,#e8cfc0 50%,#9aa3a8)"></div>
 <p class="post" style="top:87px">Maecenas pharetra est sed enim vulpu tate sollicitudin. Nam neclar nunc nec arcu suscipit pulvinar posuere.<em>April-14-2013</em></p>
</div></div>

<div class="side-box abs" style="top:769px;height:178px;background:var(--panel)"><div class="side-head">Follow us on <span style="color:#3b5b9a">FRIENDLOOP</span></div>
<div class="side-inner" style="top:24px;height:150px">
 <div class="friend" style="left:8px;top:12px"><span style="background:#6f9cc0"></span>Nadia</div>
 <div class="friend" style="left:51px;top:12px"><span style="background:#a0705a"></span>Stavro</div>
 <div class="friend" style="left:94px;top:12px"><span style="background:#7d9c6a"></span>Sorin</div>
 <div class="friend" style="left:137px;top:12px"><span style="background:#efe6e6"></span>Mathis</div>
 <div class="friend" style="left:8px;top:63px"><span style="background:#333"></span>Kavelin</div>
 <div class="friend" style="left:51px;top:63px"><span style="background:#8a8f98"></span>Kasim</div>
 <div class="friend" style="left:94px;top:63px"><span style="background:#eee"></span>Marovai</div>
 <div class="friend" style="left:137px;top:63px"><span style="background:#777"></span>Sandoval</div>
 <div class="abs" style="left:10px;top:128px;width:30px;height:11px;border:1px solid #ccc;background:#f4f4f4;font-size:6.5px;color:#3b5b9a;padding:1px 0 0 3px"><i style="display:inline-block;width:6px;height:6px;background:#3b5b9a;vertical-align:-1px"></i> Like</div>
 <div class="abs" style="left:44px;top:128px;width:16px;height:11px;border:1px solid #ccc;background:#fff;font-size:6.5px;text-align:center;padding-top:1px">3k</div>
</div></div>

<div class="side-box abs" style="top:955px;height:55px;background:var(--pink)"><div class="side-head">Subscribe for Newsletter</div>
<div class="field" style="top:26px">Enter your mail ID</div>
<svg class="abs" style="left:159px;top:27px" width="17" height="17" viewBox="0 0 17 17"><circle cx="8.5" cy="8.5" r="7.5" fill="#eee" stroke="#888"/><path d="M7 5l4 3.5L7 12Z" fill="#333"/></svg></div>

<footer class="site-footer abs"></footer>
<div class="foot-links abs">Home &nbsp;| &nbsp;About &nbsp;| &nbsp;Services &nbsp;| &nbsp;Media &nbsp;| &nbsp;Categories</div>
<div class="foot-copy abs">Copyright &nbsp;© &nbsp;2013 &nbsp;&nbsp;www.blog.fernlowdayspa.com &nbsp;&nbsp;All rights reserved.</div>
<div class="foot-share abs"><i class="s1"></i><i class="s2"></i><i class="s3"></i><i class="s4"></i><i class="s5"></i><i class="s6"></i><i class="s7"></i><i class="s8"></i></div>
</body>
</html>
```